Log In Screen Design

We have an existing website (www.velmarix4.com) and have recently developed software which requires a login screen using a similar theme from the velmarix4 website. The login screen should have a username and password. The software title is Outcome Tiered Scheduling (OTS). The VELMARIX4 log should appear on the login screen and the page should look professional.
Target Market(s)
Project Management Professionals
Industry/Entity Type
Software
Requirements
Must have
- Username and password blocks
Company Logo
Company Name - VELMARIX4 Management Ltd
Software Name - Outcome Tiered Scheduling (OTS)
Similar theme (colors) to the logo and existing website

```html
<!DOCTYPE html>
<html lang="en">
<head>
<meta charset="utf-8">
<title>Outcome Tiered Scheduling – Login</title>
<link href="https://fonts.googleapis.com/css2?family=Open+Sans:wght@400;600&display=swap" rel="stylesheet">
<style>
  :root {
    --bg-deep: #0c2646;
    --bg-mid: #24598d;
    --bg-glow: #74e6f6;
    --bg-soft: #3f86c4;
    --card-light: #f2f2f2;
    --card-dark: #bdbdbd;
    --card-edge: #ffffff;
    --tab-fill: #6a6a6a;
    --tab-text: #ffffff;
    --label: #5a5a5a;
    --field: #ffffff;
    --button: #6b6b6b;
    --brand: #6d6d6d;
    --brand-dot: #2f6fb6;
    --footer: #1a1a1a;
  }
  * { box-sizing: border-box; margin: 0; padding: 0; }
  html, body { width: 1200px; height: 1000px; overflow: hidden; }
  body {
    position: relative;
    font-family: "Open Sans", sans-serif;
    background:
      radial-gradient(ellipse 330px 150px at 1000px 290px, var(--bg-glow) 0%, rgba(116,230,246,0.5) 45%, rgba(116,230,246,0) 100%),
      radial-gradient(ellipse 420px 180px at 950px 760px, rgba(90,170,220,0.55) 0%, rgba(90,170,220,0) 100%),
      radial-gradient(ellipse 520px 300px at 500px 230px, rgba(70,140,200,0.55) 0%, rgba(70,140,200,0) 100%),
      radial-gradient(ellipse 600px 500px at 0px 1000px, var(--bg-deep) 0%, rgba(12,38,70,0) 100%),
      linear-gradient(160deg, #1d4a78 0%, var(--bg-mid) 45%, var(--bg-soft) 70%, #245f98 100%);
  }
  .login-card {
    position: absolute;
    left: 401px; top: 368px;
    width: 391px; height: 255px;
    background: linear-gradient(180deg, var(--card-light) 0%, #dedede 50%, var(--card-dark) 100%);
    border: 1px solid var(--card-edge);
    box-shadow: 0 0 12px rgba(0,0,0,0.25);
  }
  .title-tab {
    position: absolute;
    left: 73px; top: -6px;
    width: 257px; height: 39px;
  }
  .title-tab svg { position: absolute; inset: 0; }
  .title-tab h1 {
    position: relative;
    font-weight: 400;
    font-size: 17.5px;
    color: var(--tab-text);
    text-align: center;
    line-height: 39px;
    padding-top: 6px;
    line-height: 32px;
  }
  .brand {
    position: absolute;
    left: 30px; top: 72px;
    width: 125px;
    text-align: center;
  }
  .brand-dot {
    width: 86px; height: 86px;
    margin: 0 auto 14px;
    border-radius: 50%;
    background: var(--brand-dot);
  }
  .brand-name {
    font-size: 19px;
    font-weight: 400;
    color: var(--brand);
    letter-spacing: 0.5px;
  }
  .login-form { position: absolute; left: 184px; top: 88px; width: 189px; }
  .field-label {
    display: block;
    font-size: 11.5px;
    color: var(--label);
    line-height: 13px;
  }
  .field-input {
    display: block;
    width: 189px; height: 21px;
    border: 1px solid #d8d8d8;
    background: var(--field);
    margin-bottom: 13px;
  }
  .form-row { position: relative; height: 20px; margin-top: -9px; }
  .remember {
    position: absolute; left: 2px; top: 1px;
    display: flex; align-items: center; gap: 3px;
    font-size: 7px; color: var(--label);
  }
  .remember-radio {
    width: 7px; height: 7px; border-radius: 50%;
    background: #fff; border: 1px solid #888;
    position: relative;
  }
  .remember-radio::after {
    content: ""; position: absolute; left: 1.5px; top: 1.5px;
    width: 2px; height: 2px; border-radius: 50%; background: #333;
  }
  .login-button {
    position: absolute; left: 125px; top: -1px;
    width: 56px; height: 18px;
    background: var(--button);
    border: none;
    color: #fff;
    font-family: "Open Sans", sans-serif;
    font-size: 10px;
    line-height: 18px;
  }
  .company-footer {
    position: absolute; right: 16px; bottom: 8px;
    font-size: 8.5px; color: var(--footer);
  }
</style>
</head>
<body>
  <main class="login-card">
    <div class="title-tab">
      <svg width="257" height="39" viewBox="0 0 257 39" aria-hidden="true">
        <polygon points="0,0 257,0 242,33 15,33" fill="var(--tab-fill)"/>
      </svg>
      <h1>Outcome Tiered Scheduling</h1>
    </div>

    <div class="brand">
      <div class="brand-dot"></div>
      <div class="brand-name">VELMARIX4</div>
    </div>

    <form class="login-form">
      <label class="field-label" for="username">User Name</label>
      <input class="field-input" id="username" type="text">
      <label class="field-label" for="password">Password</label>
      <input class="field-input" id="password" type="password">
      <div class="form-row">
        <span class="remember"><span class="remember-radio"></span>Remember Me</span>
        <button class="login-button" type="button">Login</button>
      </div>
    </form>

    <p class="company-footer">VELMARIX4 Management Ltd</p>
  </main>
</body>
</html>
```